Vesk Architecture

We are a architectural design and build company working between scales 1/1000 to 1/1 we want people to understand our difference from our design experience and quality.we build hotels restourants and office spaces.Our company name is Vesk architecture to mind sustainability.

We want to write our adress phone and work spesifications on the card and we want our logo as backround.

Ps:you could find the logo adress and phone box numbers from the web:www.veskmimarlik-ornek.com

Target Market(s)

Who looks for experts.

Industry/Entity Type

Architecture

Requirements
Must have
• Design is over everything.
Should not have
• we don want it to be colorfull

```html
<!DOCTYPE html>
<html lang="tr">
<head>
<meta charset="utf-8">
<title>Vesk Mimarlık – Business Card</title>
<link rel="stylesheet" href="https://fonts.googleapis.com/css2?family=Jost:wght@400;500&display=swap">
<style>
  :root {
    --canvas: #ffffff;
    --cream: #e8e3a9;
    --charcoal: #2d3134;
    --ink: #2a2a27;
    --ink-soft: #5a5848;
    --card-w: 820px;
    --card-h: 490px;
  }
  * { margin: 0; padding: 0; box-sizing: border-box; }
  html, body {
    width: 1200px;
    height: 1200px;
    overflow: hidden;
    background: var(--canvas);
    font-family: "Jost", sans-serif;
  }
  .canvas { position: relative; width: 1200px; height: 1200px; }

  .card {
    position: absolute;
    width: var(--card-w);
    height: var(--card-h);
    border-radius: 30px;
    overflow: hidden;
  }
  .card--front { left: 120px; top: 90px; background: var(--cream); color: var(--ink); }
  .card--back  { left: 260px; top: 620px; background: var(--charcoal); color: var(--cream); }

  .wordmark { position: absolute; font-weight: 400; line-height: 1; }
  .wordmark__name { display: block; letter-spacing: 2px; }
  .wordmark__sub { display: block; letter-spacing: 4px; }

  .card--front .wordmark { left: 95px; top: 135px; }
  .card--front .wordmark__name { font-size: 132px; }
  .card--front .wordmark__sub { font-size: 27px; margin-top: 4px; padding-left: 4px; }

  .divider {
    position: absolute;
    left: 385px; top: 150px;
    width: 2px; height: 300px;
    background: var(--ink);
  }
  .contact { position: absolute; left: 412px; top: 150px; }
  .contact__name { font-size: 25px; font-weight: 500; letter-spacing: 0.5px; }
  .contact__role { font-size: 21px; font-weight: 400; margin-top: 4px; }
  .contact__services { font-size: 15px; color: var(--ink-soft); letter-spacing: 1px; margin-top: 6px; }
  .contact__details { list-style: none; margin-top: 26px; font-size: 16px; letter-spacing: 0.4px; }
  .contact__details li { margin-bottom: 12px; }

  .card--back .wordmark { left: 300px; top: 170px; }
  .card--back .wordmark__name { font-size: 110px; }
  .card--back .wordmark__sub { font-size: 22px; margin-top: 4px; padding-left: 4px; }
  .website {
    position: absolute;
    right: 48px; bottom: 30px;
    font-size: 17px;
    letter-spacing: 0.3px;
  }
</style>
</head>
<body>
<main class="canvas">

  <section class="card card--front" aria-label="Card front">
    <div class="wordmark">
      <span class="wordmark__name">vesk</span>
      <span class="wordmark__sub">MİMARLIK</span>
    </div>

    <div class="divider"></div>

    <div class="contact">
      <p class="contact__name">Deniz Aral KARACA</p>
      <p class="contact__role">Mimar</p>
      <p class="contact__services">Otel · Restoran · Ofis · 1/1000 – 1/1</p>
      <ul class="contact__details">
        <li>Kestane Mah. Lale Cad. Papatya Sok.</li>
        <li>No : 7 Kadiköy / ISTANBUL</li>
        <li>Tel : 0216 555 01 23</li>
        <li>Fax : 0216 555 01 45</li>
        <li>Email: info@veskmimarlik-ornek.com</li>
      </ul>
    </div>
  </section>

  <section class="card card--back" aria-label="Card back">
    <div class="wordmark">
      <span class="wordmark__name">vesk</span>
      <span class="wordmark__sub">MİMARLIK</span>
    </div>
    <p class="website">www.veskmimarlik-ornek.com</p>
  </section>

</main>
</body>
</html>
```